Web Design Project

We are looking for a new site design for the OLVEN Summit & Fair. The current site can be found at
http://olvenmeetup-example.org/
The URL is provided for reference. We want a completely different look and layout which is shown in the specifications document.
As part of the design, we want a home page, inside page and a mobile design. The mobile version is to be fairly simple and uncluttered and based on the web design - simple is key and a sample site is referenced in the specifications document.
The design you provide will be implemented in Joomla. The design winner will only need to provide the PSD or Fireworks PNG format. We anticipate creating the template coding in-house.
However, if you have experience creating Joomla templates, please let us know as we may ask you to bid separately to do that phase of the project.
We've provided a specifications document which includes wireframes of the home page, inside page, and mobile version as well as sample sites. We've also included logo files and a picture of the conference city.
For the header at the top, as indicated in the specs document, we want to keep the same overall treatment to every page. We don't want to include images from the city within the header. Instead we want a graphic treatment with the logo. In this manner, the design will be flexiable and can be used for future years.
For the home page, we've indicated that we'd like to have a banner placement implemented within the design. Please place the city image in this area with a nice graphic treatment. This might also be a good place to include the hosting city and date: Saskatoon, SK June 2-5. 2013
The wireframe is provided to illustrate the placement of content and menu items. The exact dimensions of each component can be revised as you see fit. We are also flexiable if you feel we have missed items.

```html
<!DOCTYPE html>
<html lang="en">
<head>
<meta charset="utf-8">
<title>OLVEN Summit &amp; Fair</title>
<link href="https://fonts.googleapis.com/css2?family=Ubuntu:wght@400;500;700&family=Arimo:wght@400;700&display=swap" rel="stylesheet">
<style>
:root{
  --navy:#1c3a82;
  --navy-dark:#162f6c;
  --red:#e8120f;
  --panel:#efefef;
  --text:#1a1a1a;
  --rule:#d6d6d6;
  --footer:#3b3b3b;
  --footer-text:#c9c9c9;
  --white:#ffffff;
}
*{box-sizing:border-box;margin:0;padding:0}
html,body{width:1187px;height:1200px;overflow:hidden;background:var(--white)}
body{position:relative;font-family:Arimo,Arial,sans-serif;color:var(--text)}
.abs{position:absolute}

/* header */
.site-header{left:0;top:0;width:1187px;height:146px;background:linear-gradient(#ffffff 40%,#e9e9e9)}
.brand{left:118px;top:30px;display:flex;align-items:center;gap:8px}
.brand-mark{width:26px;height:26px;border-radius:50%;background:var(--navy)}
.brand-name{font-family:Ubuntu,sans-serif;font-weight:700;font-size:24px;color:var(--navy);line-height:1}
.brand-sub{left:118px;top:64px;font-family:Ubuntu,sans-serif;font-size:11px;color:var(--navy);line-height:14px;width:150px}
.call{left:797px;top:50px;display:flex;align-items:center;gap:8px}
.call-icon{width:56px;height:56px}
.call-label{font-family:Arimo,sans-serif;font-size:18px;color:var(--navy);line-height:20px}
.call-number{font-size:24px;color:var(--red);line-height:26px}

/* nav */
.main-nav{left:0;top:146px;width:1187px;height:34px;background:var(--navy)}
.nav-item{position:absolute;top:0;height:34px;line-height:34px;font-family:Ubuntu,sans-serif;font-size:12px;color:var(--white);text-transform:uppercase}
.nav-item.is-active{top:-4px;height:38px;line-height:42px;background:var(--red);padding:0 17px;left:128px}

/* mailing */
.mailing{left:101px;top:204px;width:250px;height:311px;background:var(--navy)}
.mailing h2{position:absolute;left:23px;top:22px;font-family:Ubuntu,sans-serif;font-weight:500;font-size:20px;color:var(--white)}
.field{position:absolute;left:24px;width:191px;height:29px;background:var(--white);border:1px solid #c8c8c8;font-size:11px;color:#777;padding:8px 8px}
.field.tall{height:68px;padding-top:9px}
.go-btn{position:absolute;left:162px;top:243px;width:54px;height:26px;border-radius:13px;background:linear-gradient(#f24a43,#c70f0c);color:var(--white);font-family:Ubuntu,sans-serif;font-weight:500;font-size:14px;text-align:center;line-height:26px}

/* banner */
.banner{left:351px;top:204px;width:733px;height:311px;background:linear-gradient(180deg,#c9d4dd 0%,#a9b5b8 35%,#6f7a6a 60%,#47513b 100%)}
.banner-card{left:486px;top:244px;width:554px;height:234px;border:2px solid var(--white);border-radius:12px;background:rgba(255,255,255,.72);box-shadow:0 0 6px rgba(0,0,0,.3)}
.banner-num{left:502px;top:248px;font-family:Arimo,sans-serif;font-weight:700;font-size:58px;color:var(--red);line-height:64px}
.banner-title{left:638px;top:248px;font-family:Ubuntu,sans-serif;font-weight:500;font-size:37px;color:var(--navy);line-height:40px;letter-spacing:.5px}
.banner-place{left:644px;top:286px;font-family:Ubuntu,sans-serif;font-weight:500;font-size:21px;color:var(--text)}
.banner-text{left:497px;top:325px;width:535px;font-size:13px;line-height:20px;color:var(--text)}
.learn-btn{left:495px;top:430px;width:142px;height:37px;border-radius:8px;background:linear-gradient(#ff3b30,#d50f0b);color:var(--white);font-family:Ubuntu,sans-serif;font-size:18px;line-height:37px;padding-left:11px}

/* sidebar */
.sidebar{left:101px;top:515px;width:250px;height:546px;background:var(--panel)}
.side-title{position:absolute;font-family:Ubuntu,sans-serif;font-weight:500;font-size:20px;color:var(--navy)}
.quick-list{position:absolute;left:0;top:49px;width:250px;list-style:none}
.quick-list li{height:26px;border-bottom:1px solid var(--rule);font-size:12.5px;line-height:28px;padding-left:14px;position:relative;letter-spacing:.2px}
.quick-list li::after{content:"";position:absolute;right:9px;top:10px;border-left:5px solid var(--navy);border-top:4px solid transparent;border-bottom:4px solid transparent}
.side-note{position:absolute;left:6px;top:272px;width:240px;font-size:12px;line-height:16px;text-align:justify}
.side-link{position:absolute;left:6px;top:328px;font-size:12px;font-weight:700;font-style:italic;color:var(--navy);text-decoration:underline}
.side-small{position:absolute;left:8px;top:416px;width:240px;font-size:12px;line-height:14px;color:#333}
.social{position:absolute;top:457px;width:38px;height:38px}

/* content */
.content-title{left:369px;top:543px;font-family:Ubuntu,sans-serif;font-weight:500;font-size:20px;color:var(--red)}
.content-photo{left:369px;top:579px;width:213px;height:197px;border:1px solid #ccc;padding:3px;background:var(--white)}
.content-photo div{width:100%;height:100%;background:linear-gradient(135deg,#e5e3e0,#8e8f93 60%,#3c3f46)}
.content-text{font-size:12px;line-height:18px;color:var(--text)}
.read-more{left:988px;top:827px;width:88px;height:25px;background:#111;color:var(--white);font-size:12px;line-height:25px;padding-left:6px}
.sponsors-title{left:370px;top:885px;font-family:Ubuntu,sans-serif;font-weight:500;font-size:21px;color:var(--navy)}
.sponsor-strip{left:369px;top:922px;width:709px;height:93px;border:1px solid #ddd;background:linear-gradient(#fafafa,#e9e9e9)}
.sponsor{position:absolute;top:20px;height:59px;border:1px solid #3a5aa6;background:var(--white);display:flex;align-items:center;justify-content:center;font-family:Ubuntu,sans-serif;font-weight:700;font-size:14px;color:var(--navy)}
.strip-arrow{position:absolute;top:30px;width:20px;height:34px}

/* footer */
.site-footer{left:0;top:1090px;width:1187px;height:110px;background:var(--footer);border-top:3px solid #2a2a2a}
.footer-brand{position:absolute;left:148px;top:36px;display:flex;align-items:center;gap:7px}
.footer-brand span:first-child{width:18px;height:18px;border-radius:50%;background:#777}
.footer-brand span:last-child{font-family:Ubuntu,sans-serif;font-weight:700;font-size:20px;color:#8a8a8a}
.footer-nav{position:absolute;left:278px;top:49px;font-family:Ubuntu,sans-serif;font-size:12px;color:var(--footer-text);word-spacing:2px}
.footer-nav span{margin:0 8px}
.copyright{position:absolute;left:278px;top:73px;font-size:12px;color:var(--footer-text)}
</style>
</head>
<body>

<header class="abs site-header">
  <div class="abs brand"><span class="brand-mark"></span><span class="brand-name">OLVEN</span></div>
  <div class="abs brand-sub">Summit &amp; Fair<br>Saskatoon, SK June 2-5, 2013</div>
  <div class="abs call">
    <svg class="call-icon" viewBox="0 0 56 56" aria-hidden="true">
      <circle cx="28" cy="28" r="25" fill="#fff" stroke="#111" stroke-width="3"/>
      <path d="M20 14c3-1 5 5 3 7l-2 2c1 4 5 9 9 11l2-2c2-2 8 0 7 3l-1 3c-1 2-5 3-9 1-7-4-13-11-15-18-1-4 1-7 3-7z" fill="#111"/>
    </svg>
    <div><div class="call-label">Call Us Today</div><div class="call-number">123-456-7890</div></div>
  </div>
</header>

<nav class="abs main-nav">
  <span class="nav-item is-active">Home</span>
  <span class="nav-item" style="left:231px">About</span>
  <span class="nav-item" style="left:329px">Schedule</span>
  <span class="nav-item" style="left:450px">Registration</span>
  <span class="nav-item" style="left:588px">Exhibitors</span>
  <span class="nav-item" style="left:715px">Education</span>
  <span class="nav-item" style="left:848px">Sponsors</span>
  <span class="nav-item" style="left:966px">Connect</span>
</nav>

<section class="abs mailing">
  <h2>Join Our Mailing List</h2>
  <div class="field" style="top:78px">Username</div>
  <div class="field" style="top:117px">Enter E-mail Adress</div>
  <div class="field tall" style="top:159px">Address</div>
  <div class="go-btn">Go</div>
</section>

<div class="abs banner" role="img" aria-label="Photo of the Saskatoon skyline and river bridges at dusk"></div>
<div class="abs banner-card"></div>
<div class="abs banner-num">29th</div>
<div class="abs banner-title">CONFERENCE &amp; EXPO</div>
<div class="abs banner-place">Saskatoon, SK june 2-5, 2013</div>
<p class="abs banner-text">The 2013 OLVEN Summit will be held June 2-5 in Saskatoon!&nbsp;&nbsp; Please review the attached document containing both the Speaker Background information and the Speaker Application form.OLVEN invites you to consider submitting a Speaker Application and share your valuable information and expertise.</p>
<div class="abs learn-btn">Learn More &#187;</div>

<aside class="abs sidebar">
  <h2 class="side-title" style="left:13px;top:22px">Quick Links</h2>
  <ul class="quick-list">
    <li>Live Feed</li>
    <li>Agenda/Speakers</li>
    <li>Agenda at a Glance</li>
    <li>About the RPC</li>
    <li>Conference Themes</li>
    <li>Who Should Attend?</li>
    <li>Conference Objectives</li>
  </ul>
  <p class="side-note">The 2013 OLVEN Summit also provides a wide variety of exhibition and sponsorship opportunities.</p>
  <span class="side-link">Dana Whitcombe</span>
  <h2 class="side-title" style="left:7px;top:384px">Stay Connected</h2>
  <p class="side-small">Keep in touch with OLVEN using the variety of social media:</p>
  <svg class="social" style="left:23px" viewBox="0 0 38 38" aria-hidden="true"><circle cx="19" cy="19" r="17" fill="#2f6fb5" stroke="#9fb8d6" stroke-width="2"/></svg>
  <svg class="social" style="left:75px" viewBox="0 0 38 38" aria-hidden="true"><circle cx="19" cy="19" r="17" fill="#2f6fb5" stroke="#9fb8d6" stroke-width="2"/></svg>
  <svg class="social" style="left:126px" viewBox="0 0 38 38" aria-hidden="true"><circle cx="19" cy="19" r="17" fill="#2f6fb5" stroke="#9fb8d6" stroke-width="2"/></svg>
  <svg class="social" style="left:176px" viewBox="0 0 38 38" aria-hidden="true"><circle cx="19" cy="19" r="17" fill="#333" stroke="#aaa" stroke-width="2"/><path d="M19 11v16M11 19h16" stroke="#fff" stroke-width="4"/></svg>
</aside>

<h1 class="abs content-title">Come to Saskatoon in 2013.</h1>
<div class="abs content-photo" role="img" aria-label="Photo of two colleagues working together at a laptop"><div></div></div>
<p class="abs content-text" style="left:594px;top:579px;width:486px">The 2012 Nanaimo Conference was a great success - Now is time to start planning for 2013 in Saskatoon. The annual OLVEN Summit provides an opportunity for RIM professionals to expand their knowledge, meet with exhibitors, and network with their peers. Average attendance at an OLVEN Summit continues to grow and we anticipate more than 300 delegates&nbsp; variety of professional backgrounds/levels at the 2012 conference.</p>
<p class="abs content-text" style="left:594px;top:704px;width:486px">Conference delegates typically work in a wide variety of industries including government, not-for-profit entities, and the private sector.If you have questions about the education program at the 2013</p>
<p class="abs content-text" style="left:371px;top:780px;width:700px">The annual OLVEN Summit provides an opportunity for RIM professionals to expand their knowledge, meet with exhibitors, and network with their peers.</p>
<div class="abs read-more">read more &#8594;</div>

<h2 class="abs sponsors-title">Our Sponsors</h2>
<div class="abs sponsor-strip">
  <svg class="strip-arrow" style="left:12px" viewBox="0 0 20 34" aria-hidden="true"><path d="M16 2L4 17l12 15" fill="none" stroke="#bbb" stroke-width="2"/></svg>
  <div class="sponsor" style="left:50px;width:108px">NORTHLINK</div>
  <div class="sponsor" style="left:190px;width:88px;border-color:#ccc">Vertexa</div>
  <div class="sponsor" style="left:311px;width:86px;font-size:11px">Prairie Towers</div>
  <div class="sponsor" style="left:429px;width:90px">Kestrel</div>
  <div class="sponsor" style="left:552px;width:96px">Ridgeway</div>
  <svg class="strip-arrow" style="left:675px" viewBox="0 0 20 34" aria-hidden="true"><path d="M4 2l12 15L4 32" fill="none" stroke="#bbb" stroke-width="2"/></svg>
</div>

<footer class="abs site-footer">
  <div class="footer-brand"><span></span><span>OLVEN</span></div>
  <div class="footer-nav">HOME<span>|</span>ABOUT<span>|</span>REGISTRATION<span>|</span>EXHIBITORS<span>|</span>EDUCATION</div>
  <div class="copyright">Copyright &copy; 2012. All Rights Reserved. Designed and Developed.</div>
</footer>

</body>
</html>
```